Letterhead and Business card for Construction company

We need a letterhead and business card with our new company logo. We are based in NY. We develop and build properties.

The design should incorporate some unique feature from the logo (shape, font...). it should look like an extension from it.

Design should be clean and elegant, professional, not too busy.

The letterhead should include:
Logo (attached)
Address
Phone
Email

Please find the attached logo images and AI file.

Target Market(s)

Construction industry professionals

Industry/Entity Type

Construction, Development

Font styles to use
Sans Serif

Colors

Designer to choose colors to be used in the design.

Requirements
Must have
• Design should incorporate logo elements, additional assets are welcome. I'd like to see some other shapes / images invorporated too.

```html
<!DOCTYPE html>
<html lang="en">
<head>
<meta charset="utf-8">
<title>Halvard Builders Letterhead</title>
<link rel="stylesheet" href="https://fonts.googleapis.com/css2?family=Montserrat:wght@400;700;800&display=swap">
<style>
  :root {
    --backdrop: #bdbcbb;
    --paper: #ffffff;
    --ink: #2f2e2f;
    --ink-soft: #3a3a3a;
    --accent: #f0822d;
    --rule: #4a4a4a;
    --watermark-warm: rgba(240, 130, 45, 0.07);
    --watermark-grey: rgba(120, 120, 120, 0.05);
  }
  * { margin: 0; padding: 0; box-sizing: border-box; }
  html, body {
    width: 1200px;
    height: 939px;
    overflow: hidden;
    background: var(--backdrop);
  }
  .canvas {
    position: relative;
    width: 1200px;
    height: 939px;
  }
  .letterhead {
    position: absolute;
    left: 289px;
    top: 30px;
    width: 622px;
    height: 880px;
    background: var(--paper);
    overflow: hidden;
    font-family: "Montserrat", sans-serif;
    color: var(--ink);
  }
  .brand {
    position: absolute;
    left: 50px;
    top: 66px;
    display: flex;
    align-items: center;
    gap: 12px;
  }
  .brand-square {
    width: 40px;
    height: 40px;
    background: var(--accent);
  }
  .brand-name {
    font-weight: 800;
    font-size: 26px;
    line-height: 1.05;
    letter-spacing: 0.5px;
    color: var(--ink);
    text-transform: uppercase;
  }
  .contact {
    position: absolute;
    left: 438px;
    top: 49px;
    list-style: none;
    font-size: 12.5px;
    line-height: 15px;
    color: var(--ink-soft);
  }
  .contact li {
    display: flex;
    align-items: flex-start;
    gap: 7px;
    margin-bottom: 0.5px;
  }
  .contact li.address { margin-top: 2px; }
  .contact svg {
    flex: none;
    width: 10px;
    height: 10px;
    margin-top: 3px;
    fill: var(--ink);
  }
  .header-rule {
    position: absolute;
    left: 50px;
    top: 144px;
    width: 536px;
    height: 1px;
    background: var(--rule);
  }
  .watermark {
    position: absolute;
    left: 141px;
    top: 266px;
    width: 325px;
    height: 410px;
    background:
      radial-gradient(ellipse at 65% 40%, var(--watermark-warm) 0%, rgba(255,255,255,0) 60%),
      radial-gradient(ellipse at 35% 70%, var(--watermark-grey) 0%, rgba(255,255,255,0) 65%);
  }
  .footer-wave {
    position: absolute;
    left: 0;
    bottom: 0;
    width: 622px;
    height: 70px;
  }
</style>
</head>
<body>
<div class="canvas">
  <section class="letterhead">
    <div class="brand">
      <span class="brand-square"></span>
      <span class="brand-name">Halvard<br>Builders</span>
    </div>

    <ul class="contact">
      <li>
        <svg viewBox="0 0 24 24" aria-hidden="true"><path d="M6.6 10.8a15.1 15.1 0 0 0 6.6 6.6l2.2-2.2a1 1 0 0 1 1-.25 11.4 11.4 0 0 0 3.6.57 1 1 0 0 1 1 1V20a1 1 0 0 1-1 1A17 17 0 0 1 3 4a1 1 0 0 1 1-1h3.5a1 1 0 0 1 1 1c0 1.25.2 2.45.57 3.57a1 1 0 0 1-.25 1z"/></svg>
        <span>044-123 456 789</span>
      </li>
      <li>
        <svg viewBox="0 0 24 24" aria-hidden="true"><path d="M2 5h20v14H2z M3.5 6.5 12 13l8.5-6.5" stroke="#fff" stroke-width="1.6"/></svg>
        <span>info@webname.com</span>
      </li>
      <li>
        <svg viewBox="0 0 24 24" aria-hidden="true"><circle cx="12" cy="12" r="10"/><path d="M2 12h20M12 2c3 3 3 17 0 20M12 2c-3 3-3 17 0 20" stroke="#fff" stroke-width="1.4" fill="none"/></svg>
        <span>www.websitename.com</span>
      </li>
      <li class="address">
        <svg viewBox="0 0 24 24" aria-hidden="true"><path d="M12 2a7 7 0 0 0-7 7c0 5.2 7 13 7 13s7-7.8 7-13a7 7 0 0 0-7-7zm0 9.5A2.5 2.5 0 1 1 12 6.5a2.5 2.5 0 0 1 0 5z"/></svg>
        <span>421, Address line here<br>Country Name, 45452</span>
      </li>
    </ul>

    <div class="header-rule"></div>

    <div class="watermark" role="img" aria-label="Faint brand watermark in soft grey and orange"></div>

    <svg class="footer-wave" viewBox="0 0 622 70" preserveAspectRatio="none" aria-hidden="true">
      <path d="M0 16 C 90 36, 200 42, 320 40 C 430 36, 520 10, 622 12 L622 70 L0 70 Z" fill="var(--accent)"/>
      <path d="M0 24 C 90 42, 210 48, 320 45 C 440 40, 520 22, 622 24 L622 70 L0 70 Z" fill="var(--paper)"/>
      <path d="M0 27 C 100 46, 220 52, 330 48 C 450 42, 530 28, 622 32 L622 70 L0 70 Z" fill="var(--ink)"/>
    </svg>
  </section>
</div>
</body>
</html>
```